Bramwell Ridge Minerals

Looking for a cool, glossy business card...white with our logo on one side and then the a smaller version of the logo on the other side (top left hand corner) and then the name and position of the person next to it, and then the office address and email address on the bottom left hand corner and the phone numbers & email address on the bottom right hand corner. I have the logo already...can pass it on when you're ready.

```html
<!DOCTYPE html>
<html lang="en">
<head>
<meta charset="utf-8">
<title>Bramwell Ridge Minerals – Business Card</title>
<link href="https://fonts.googleapis.com/css2?family=Cinzel:wght@400;600&family=Open+Sans:wght@400;600&display=swap" rel="stylesheet">
<style>
  :root {
    --stage: #d9dce1;
    --card: #ffffff;
    --card-shade: #f1f1f3;
    --ink: #2a2a2e;
    --ink-soft: #4a4a52;
    --red: #b3191f;
    --blue: #2d3f9e;
    --rule: #e3e4e8;
  }
  * { box-sizing: border-box; margin: 0; padding: 0; }
  html, body { width: 1200px; height: 900px; overflow: hidden; }
  body {
    background: var(--stage);
    display: flex;
    flex-direction: column;
    align-items: center;
    justify-content: center;
    gap: 50px;
    font-family: "Open Sans", Arial, sans-serif;
    color: var(--ink);
  }
  .card {
    width: 640px;
    height: 366px;
    background: linear-gradient(160deg, var(--card) 55%, var(--card-shade));
    box-shadow: 0 6px 18px rgba(0,0,0,.18);
    position: relative;
  }
  /* front */
  .card--front { display: flex; align-items: center; justify-content: center; }
  .brand {
    display: flex; align-items: center; gap: 14px;
    font-family: "Cinzel", Georgia, serif;
    font-weight: 400;
    color: var(--ink);
    letter-spacing: .04em;
  }
  .brand__mark { width: 22px; height: 22px; background: var(--blue); }
  .brand--large { font-size: 34px; }
  .brand--small { font-size: 14px; gap: 8px; }
  .brand--small .brand__mark { width: 12px; height: 12px; }
  /* back */
  .card--back .brand--small { position: absolute; left: 34px; top: 34px; }
  .person { position: absolute; right: 48px; top: 110px; text-align: right; }
  .person__name {
    font-family: "Cinzel", Georgia, serif;
    font-weight: 600; font-size: 30px; letter-spacing: .06em; color: var(--ink);
  }
  .person__role {
    font-family: "Cinzel", Georgia, serif;
    font-size: 17px; color: var(--red); margin-top: 10px; letter-spacing: .05em;
  }
  .divider-ornament {
    position: absolute; left: 250px; top: 196px;
    width: 110px; height: 10px; border-radius: 5px;
    background: linear-gradient(90deg, var(--blue), var(--red));
    opacity: .35;
  }
  .contact { position: absolute; list-style: none; font-size: 13px; color: var(--ink-soft); }
  .contact li { display: flex; align-items: center; gap: 10px; margin-top: 10px; }
  .contact svg { width: 15px; height: 15px; fill: none; stroke: var(--blue); stroke-width: 1.8; }
  .contact--left { left: 34px; top: 120px; }
  .contact--right { right: 48px; bottom: 36px; text-align: right; }
  .contact--right li { justify-content: flex-end; }
</style>
</head>
<body>

<section class="card card--front" aria-label="Card front">
  <div class="brand brand--large">
    <span class="brand__mark"></span>
    <span class="brand__name">Bramwell Ridge Minerals</span>
  </div>
</section>

<section class="card card--back" aria-label="Card back">
  <div class="brand brand--small">
    <span class="brand__mark"></span>
    <span class="brand__name">Bramwell Ridge Minerals</span>
  </div>

  <ul class="contact contact--left">
    <li>
      <svg viewBox="0 0 16 16"><circle cx="8" cy="8" r="6.5"/><path d="M1.5 8h13M8 1.5c2.5 2.5 2.5 10.5 0 13M8 1.5c-2.5 2.5-2.5 10.5 0 13"/></svg>
      <span>www.bramwellridge.com</span>
    </li>
    <li>
      <svg viewBox="0 0 16 16"><path d="M8 15s5-5 5-8.5A5 5 0 0 0 3 6.5C3 10 8 15 8 15z"/><circle cx="8" cy="6.5" r="1.8"/></svg>
      <span>Street, Area, City, Country</span>
    </li>
  </ul>

  <div class="divider-ornament" role="img" aria-label="Row of small red and blue stars"></div>

  <div class="person">
    <p class="person__name">Elena Marsh</p>
    <p class="person__role">Director</p>
  </div>

  <ul class="contact contact--right">
    <li>
      <span>512 408 3196</span>
      <svg viewBox="0 0 16 16"><path d="M4 1.5l2.2 3-1.4 1.6a8 8 0 0 0 5.1 5.1l1.6-1.4 3 2.2-1.2 2.3C8 14.5 1.5 8 1.7 2.7z"/></svg>
    </li>
    <li>
      <span>info@bramwellridge.com</span>
      <svg viewBox="0 0 16 16"><rect x="1.5" y="3.5" width="13" height="9"/><path d="M1.5 3.5L8 9l6.5-5.5"/></svg>
    </li>
  </ul>
</section>

</body>
</html>
```